We need to design Labels of one of Our Brand QuelaVant Lotion.

The purpose of this product is to keep mosquitoes away.
There are 3 variants of this lotion. So we need 3 designs for the product. These variants details are mentioned below:

1) Mosquito Repellent Lotion with Lavender Fragrance.
2) Mosquito Repellent Lotion with Natural Ingredients.
3) Mosquito Repellent Lotion for kids.

Kindly note the bottle will be WHITE for all the variants. Cap will of the bottle will be with accordance to the color of label. In the picture it is red just for presentation.

Kindly share design of Repellent Lotion with Lavendar Fragrance initially and if we give your positive feedback, then you may add further variants of the design.

The bottle shape is attached along with keylines. Also attaching logo. If there is any other option for logo, you can suggest which we would probably keep our existing logo.

Target Market(s)

B+, B, C+

Industry/Entity Type

Product

Colors
a54499
6b449b

Requirements
Must have
• Mosquito
• 100ml
Nice to have
• Purple color as background
Should not have
• Lavendar flower

```html
<!DOCTYPE html>
<html lang="en">
<head>
<meta charset="utf-8">
<title>QuelaVant Mosquito Repellent Lotion – Lavender Label</title>
<link rel="stylesheet" href="https://fonts.googleapis.com/css2?family=Anton&family=Oswald:wght@500;600;700&family=Open+Sans:wght@400;800&display=swap">
<style>
  :root{
    --bg:#ececec;
    --ink:#111111;
    --keyline:#7a0a78;
    --purple-deep:#44004e;
    --purple:#7a0077;
    --magenta:#ff4fc0;
    --drop-light:#f2c8fb;
    --drop-mid:#d9a0e4;
    --red:#c4080f;
    --brand-white:#ffffff;
    --name-yellow:#f4f620;
    --name-outline:#1c0f6b;
    --cream:#f8f5c4;
    --badge-blue:#1b2b87;
    --badge-rim:#f3f08a;
  }
  html,body{margin:0;padding:0;overflow:hidden;background:var(--bg);}
  .canvas{width:1200px;height:1190px;position:relative;}
  .artboard{display:block;width:1200px;height:1190px;}
  .dim-label{font-family:"Open Sans",sans-serif;font-size:30px;fill:var(--ink);}
  .brand-name{font-family:"Oswald",sans-serif;font-weight:700;font-size:56px;fill:var(--brand-white);}
  .badge-text{font-family:"Open Sans",sans-serif;font-weight:800;font-size:40px;fill:#ffffff;}
  .product-name{font-family:"Anton",sans-serif;paint-order:stroke;stroke:var(--name-outline);stroke-width:9px;stroke-linejoin:round;}
  .product-name.first{fill:#ffffff;font-size:138px;}
  .product-name.second{fill:var(--name-yellow);font-size:118px;}
  .product-type{font-family:"Anton",sans-serif;font-size:76px;fill:#e9e9ee;paint-order:stroke;stroke:#6a2a6a;stroke-width:5px;stroke-linejoin:round;}
  .variant{font-family:"Oswald",sans-serif;font-weight:600;font-size:42px;fill:var(--cream);}
  .volume{font-family:"Oswald",sans-serif;font-weight:500;font-size:46px;fill:#ffffff;}
</style>
</head>
<body>
<div class="canvas">
<svg class="artboard" viewBox="0 0 1494 1481" preserveAspectRatio="none" xmlns="http://www.w3.org/2000/svg">
  <defs>
    <linearGradient id="labelBody" x1="0" y1="0" x2="0" y2="1">
      <stop offset="0" stop-color="#7a0077"/>
      <stop offset="0.75" stop-color="#6a006a"/>
      <stop offset="1" stop-color="#44004e"/>
    </linearGradient>
    <linearGradient id="dropFill" x1="0" y1="0" x2="1" y2="0">
      <stop offset="0" stop-color="#b070c4"/>
      <stop offset="0.3" stop-color="#f2c8fb"/>
      <stop offset="1" stop-color="#f2c8fb"/>
    </linearGradient>
    <linearGradient id="badgeFill" x1="0" y1="1" x2="1" y2="0">
      <stop offset="0" stop-color="#5fc4e8"/>
      <stop offset="0.5" stop-color="#2d4aa8"/>
      <stop offset="1" stop-color="#1b2b87"/>
    </linearGradient>
    <clipPath id="labelClip">
      <path d="M495,290 C495,240 600,205 770,205 C940,205 1045,240 1045,285 C1035,400 1055,600 1053,760 C1050,950 1010,1150 998,1260 C992,1290 970,1300 940,1300 L600,1300 C570,1300 545,1290 540,1260 C525,1150 490,950 488,760 C486,600 500,400 495,290 Z"/>
    </clipPath>
  </defs>

  <!-- dimension guides -->
  <g class="dimensions" stroke="var(--ink)" stroke-width="2" fill="none">
    <line x1="495" y1="180" x2="1045" y2="180"/>
    <line x1="461" y1="226" x2="461" y2="1302"/>
  </g>
  <g class="dimension-arrows" fill="var(--keyline)">
    <polygon points="487,180 503,172 503,188"/>
    <polygon points="1053,180 1037,172 1037,188"/>
    <polygon points="461,217 453,233 469,233"/>
    <polygon points="461,1311 453,1295 469,1295"/>
  </g>
  <text class="dim-label" x="758" y="170" text-anchor="middle">44 mm</text>
  <text class="dim-label" x="0" y="0" text-anchor="middle" transform="translate(447,773) rotate(-90)">85 mm</text>

  <!-- label -->
  <g class="label" clip-path="url(#labelClip)">
    <rect x="480" y="200" width="580" height="1110" fill="url(#labelBody)"/>
    <polygon class="brand-corner" points="480,200 745,200 490,520 480,520" fill="var(--red)"/>
    <path class="drop-rim" d="M740,205 C900,300 1040,520 1030,760 C1020,960 900,1110 760,1110 C620,1110 500,1020 480,960 L480,520 Z" fill="#8a0a80"/>
    <path class="drop-edge" d="M745,207 C890,300 1030,520 1020,750 C1010,940 880,1070 760,1070 C640,1070 520,1010 490,985 L490,515 Z" fill="var(--magenta)"/>
    <path class="drop-inner" d="M745,215 C870,310 1000,520 990,740 C980,900 890,1010 790,1030 L520,990 L490,520 Z" fill="url(#dropFill)"/>
    <path class="drop-band" d="M495,905 C640,790 850,760 980,748 C985,880 900,1020 780,1045 C660,1050 540,1010 495,985 Z" fill="var(--magenta)" opacity="0.85"/>
    <path class="mosquito-art" role="img" aria-label="Mosquito illustration: a large faint mosquito silhouette with a smaller purple mosquito in front" d="M580,610 C650,520 760,440 880,400 C900,520 930,650 970,780 C860,790 700,780 600,760 C585,700 578,650 580,610 Z" fill="var(--drop-mid)" opacity="0.7"/>
  </g>

  <!-- brand -->
  <g class="brand-mark">
    <text class="brand-name" x="585" y="348" text-anchor="middle" transform="rotate(-38 585 330)">Kestro</text>
    <circle cx="668" cy="290" r="5" fill="var(--brand-white)"/>
  </g>

  <!-- new badge -->
  <g class="new-badge" transform="rotate(-14 928 328)">
    <ellipse cx="928" cy="328" rx="66" ry="43" fill="url(#badgeFill)" stroke="var(--badge-rim)" stroke-width="3"/>
    <text class="badge-text" x="928" y="343" text-anchor="middle">NEW</text>
  </g>

  <!-- product name -->
  <g class="product-name-block">
    <text class="product-name first" x="705" y="515" text-anchor="middle" textLength="240" lengthAdjust="spacingAndGlyphs" transform="rotate(-8 705 460)">QUELA</text>
    <text class="product-name second" x="880" y="565" text-anchor="middle" textLength="210" lengthAdjust="spacingAndGlyphs" transform="rotate(-8 880 510)">VANT</text>
  </g>

  <!-- product type -->
  <g class="product-type-block" transform="skewX(-10)">
    <text class="product-type" x="912" y="870" text-anchor="middle" textLength="370" lengthAdjust="spacingAndGlyphs">MOSQUITO</text>
    <text class="product-type" x="920" y="948" text-anchor="middle" textLength="395" lengthAdjust="spacingAndGlyphs">REPELLENT</text>
    <text class="product-type" x="935" y="1026" text-anchor="middle" textLength="255" lengthAdjust="spacingAndGlyphs">LOTION</text>
  </g>

  <!-- variant and volume -->
  <text class="variant" x="775" y="1162" text-anchor="middle" textLength="275" lengthAdjust="spacingAndGlyphs">WITH LAVENDER</text>
  <text class="variant" x="775" y="1210" text-anchor="middle" textLength="195" lengthAdjust="spacingAndGlyphs">FRAGRANCE</text>
  <text class="volume" x="772" y="1281" text-anchor="middle">100ml</text>
</svg>
</div>
</body>
</html>
```